Business Card Design for new logo

Business card Design for new logo. Follow colors from logo.
The company has offices in multiple comtries
Want to have some bulltes on the countries and also on the main services

Something like
USA*Dominican Republic*LATAM

Consulting*Healthcare IT*Tranformation

Industry/Entity Type

Information Technology

Contact Information for Business Card

Address, Phones, countries, name and position

Miron castell

Founder and CEO

947 Quarry Ln
Mill haven, PA 16835

Mcastell@novelquin.com

www.novelquin.com

717-352-6081

828-444-4444

```html
<!DOCTYPE html>
<html lang="en">
<head>
<meta charset="utf-8">
<title>Novelquin Health – Business Card</title>
<link rel="stylesheet" href="https://fonts.googleapis.com/css2?family=Source+Sans+3:wght@400;600&display=swap">
<style>
  :root {
    --brand-blue: #3a69a4;
    --brand-blue-text: #2f5b9c;
    --accent-orange: #d6773e;
    --card-white: #ffffff;
    --page-bg: #e9e7e3;
    --ink-light: #ffffff;
  }
  * { box-sizing: border-box; margin: 0; padding: 0; }
  html, body {
    width: 1200px; height: 1200px; overflow: hidden;
    background: var(--page-bg);
    font-family: "Source Sans 3", sans-serif;
  }
  .canvas { position: relative; width: 1200px; height: 1200px; }
  .card {
    position: absolute; left: 170px; width: 860px; height: 491px;
    background: var(--card-white);
    box-shadow: 0 6px 18px rgba(0,0,0,0.12);
    overflow: hidden;
  }
  .card--front { top: 80px; }
  .card--back { top: 630px; }

  .wordmark {
    position: absolute; display: flex; flex-direction: column; align-items: center;
    color: var(--brand-blue-text); font-weight: 600; white-space: nowrap;
  }
  .wordmark__dot { border-radius: 50%; background: var(--accent-orange); }
  .card--front .wordmark { left: 0; right: 0; top: 110px; font-size: 60px; gap: 16px; }
  .card--front .wordmark__dot { width: 56px; height: 56px; }
  .card--back .wordmark { left: 20px; width: 340px; top: 210px; font-size: 38px; gap: 12px; }
  .card--back .wordmark__dot { width: 40px; height: 40px; }

  .focus-lines {
    position: absolute; left: 0; right: 0; top: 330px;
    list-style: none; text-align: center;
    color: var(--brand-blue-text); font-size: 24px; font-weight: 400; line-height: 1.6;
  }
  .focus-lines__sep { color: var(--accent-orange); margin: 0 10px; }

  .back-panel { position: absolute; inset: 0; }

  .identity {
    position: absolute; left: 430px; width: 410px; top: 36px;
    color: var(--ink-light); text-align: center; font-weight: 600;
  }
  .identity__name { font-size: 36px; line-height: 1.15; }
  .identity__title { font-size: 34px; line-height: 1.2; }
  .identity__phones {
    font-size: 25px; margin-top: 6px;
    display: flex; align-items: center; justify-content: center; gap: 8px;
  }
  .identity__phones svg { width: 22px; height: 22px; }

  .contact-row {
    position: absolute; display: flex; align-items: center; gap: 22px;
    color: var(--ink-light); font-size: 24px; font-weight: 400; line-height: 1.2;
  }
  .contact-row__icon {
    width: 60px; height: 46px; flex: none;
    background: var(--accent-orange);
    display: flex; align-items: center; justify-content: center;
  }
  .contact-row__icon svg { width: 32px; height: 28px; }
  .contact-row--email { left: 368px; top: 250px; }
  .contact-row--web { left: 386px; top: 325px; }
  .contact-row--address { left: 404px; top: 400px; }
</style>
</head>
<body>
<main class="canvas">

  <section class="card card--front" aria-label="Card front">
    <div class="wordmark">
      <span class="wordmark__dot"></span>
      <span class="wordmark__name">Novelquin Health</span>
    </div>
    <ul class="focus-lines">
      <li>USA<span class="focus-lines__sep">•</span>Dominican Republic<span class="focus-lines__sep">•</span>LATAM</li>
      <li>Consulting<span class="focus-lines__sep">•</span>Healthcare IT<span class="focus-lines__sep">•</span>Transformation</li>
    </ul>
  </section>

  <section class="card card--back" aria-label="Card back">
    <svg class="back-panel" viewBox="0 0 860 491" width="860" height="491" aria-hidden="true">
      <polygon points="330,0 860,0 860,491 430,491" fill="var(--brand-blue)"/>
    </svg>

    <div class="wordmark">
      <span class="wordmark__dot"></span>
      <span class="wordmark__name">Novelquin Health</span>
    </div>

    <div class="identity">
      <p class="identity__name">Miron castell</p>
      <p class="identity__title">Founder and CEO</p>
      <p class="identity__phones">
        <svg viewBox="0 0 24 24" aria-hidden="true"><path fill="#fff" d="M6.6 10.8a15 15 0 0 0 6.6 6.6l2.2-2.2c.3-.3.7-.4 1-.2 1.1.4 2.3.6 3.6.6.6 0 1 .4 1 1V20c0 .6-.4 1-1 1A17 17 0 0 1 3 4c0-.6.4-1 1-1h3.5c.6 0 1 .4 1 1 0 1.3.2 2.5.6 3.6.1.3 0 .7-.2 1z"/></svg>
        <span>717-352-6081 / 828-444-4444</span>
      </p>
    </div>

    <div class="contact-row contact-row--email">
      <span class="contact-row__icon">
        <svg viewBox="0 0 32 24" aria-hidden="true"><rect x="2" y="3" width="28" height="18" fill="none" stroke="#fff" stroke-width="2"/><path d="M2 3l14 11L30 3M2 21l10-9M30 21l-10-9" fill="none" stroke="#fff" stroke-width="2"/></svg>
      </span>
      <span>Mcastell@novelquin.com</span>
    </div>

    <div class="contact-row contact-row--web">
      <span class="contact-row__icon">
        <svg viewBox="0 0 28 28" aria-hidden="true"><circle cx="14" cy="14" r="5" fill="none" stroke="#fff" stroke-width="2.5"/><path d="M19 9v7c0 2 3 2.5 4 0.5A10 10 0 1 0 18 23" fill="none" stroke="#fff" stroke-width="2.5" stroke-linecap="round"/></svg>
      </span>
      <span>www.novelquin.com</span>
    </div>

    <div class="contact-row contact-row--address">
      <span class="contact-row__icon">
        <svg viewBox="0 0 24 28" aria-hidden="true"><path d="M12 2a8 8 0 0 0-8 8c0 6 8 14 8 14s8-8 8-14a8 8 0 0 0-8-8z" fill="none" stroke="#fff" stroke-width="2.2"/><circle cx="12" cy="10" r="3" fill="none" stroke="#fff" stroke-width="2.2"/></svg>
      </span>
      <span>947 Quarry Ln<br>Mill haven, PA 16835</span>
    </div>
  </section>

</main>
</body>
</html>
```